plain square mark valdremo remodel

Redesign plain square mark page to match website style with more dynamic capabilities, messaging, commerce, etc.

My website address is:
Www.valdremo.consulting for corporate styling, and flavour of approach and service offered.

Target Market(s)

Small, Medium Enterprise looking for business coaching and single entrepreneurs startups looking for advice and coaching.

Font styles to use
Sans Serif

Colors
276eb1

Requirements
Must have
• Match plain square mark page style to website for branding.
• Contact information
• Services offered
• Links to website, email, Twitter, blogging. Messaging.
• (Will upload images and other data soonest).
Nice to have
• E-commerce,

```html
<!DOCTYPE html>
<html lang="en">
<head>
<meta charset="utf-8">
<title>VL Consulting – Page About</title>
<link rel="stylesheet" href="https://fonts.googleapis.com/css2?family=Roboto:wght@400;500;700&family=Roboto+Condensed:wght@400;700&family=Open+Sans:wght@300;400&display=swap">
<style>
:root{
  --bar:#4267b2;
  --page-bg:#e9ebee;
  --card:#ffffff;
  --line:#dddfe2;
  --text:#1d2129;
  --muted:#90949c;
  --link:#385898;
  --brand:#276eb1;
  --brand-dark:#0b4a8c;
  --brand-deep:#093d7a;
  --photo-a:#5b8fc4;
  --photo-b:#a9c6e3;
  --green:#42b72a;
  --alert:#fa3e3e;
}
*{box-sizing:border-box;margin:0;padding:0}
html,body{width:1200px;height:945px;overflow:hidden}
body{position:relative;background:var(--page-bg);font-family:"Roboto",Arial,sans-serif;color:var(--text)}

/* top bar */
.topbar{position:absolute;left:0;top:0;width:1200px;height:48px;background:var(--bar);border-bottom:1px solid #29487d}
.topbar__mark{position:absolute;left:11px;top:10px;width:28px;height:28px;background:#fff;border-radius:3px}
.topbar__search{position:absolute;left:46px;top:10px;width:512px;height:28px;background:#fff;border-radius:3px;font-size:15px;line-height:28px;padding-left:8px}
.topbar__search-btn{position:absolute;right:0;top:0;width:50px;height:28px;background:#f6f7f9;border-left:1px solid var(--line)}
.topbar__nav{position:absolute;left:670px;top:0;height:48px;display:flex;align-items:center;color:#fff;font-size:14px;font-weight:700}
.topbar__user{display:flex;align-items:center;gap:8px;padding-right:14px;border-right:1px solid #5b7bc0}
.topbar__avatar{width:26px;height:26px;border-radius:50%;background:#8a7f6e}
.topbar__link{padding:0 14px;border-right:1px solid #5b7bc0}
.topbar__icons{display:flex;gap:16px;margin-left:18px;align-items:center}
.topbar__icon{position:relative;width:24px;height:24px;border-radius:50%;background:#1d2f5a}
.topbar__badge{position:absolute;right:-6px;top:-6px;background:var(--alert);color:#fff;font-size:10px;line-height:14px;padding:0 4px;border-radius:3px;border:1px solid var(--bar)}

/* left column */
.sidebar{position:absolute;left:0;top:48px;width:230px}
.profile-pic{position:absolute;left:10px;top:14px;width:208px;height:208px;border-radius:50%;background:#fff;border:4px solid #fff;box-shadow:0 0 0 1px var(--line);display:flex;flex-direction:column;align-items:center;justify-content:center;gap:12px}
.profile-pic__dot{width:60px;height:60px;border-radius:50%;background:var(--brand-dark)}
.profile-pic__name{font-family:"Open Sans",sans-serif;font-size:24px;color:var(--brand-dark)}
.page-name{position:absolute;left:11px;top:240px;font-size:23px;font-weight:500}
.page-handle{position:absolute;left:11px;top:272px;font-size:16px;font-weight:700;color:var(--muted)}
.page-nav{position:absolute;left:5px;top:310px;width:213px;list-style:none}
.page-nav li{height:37px;line-height:37px;padding-left:10px;font-size:15px;color:var(--text);border-radius:2px}
.page-nav .is-active{background:#f6f7f9;font-weight:700;border:1px solid var(--line)}
.create-page{position:absolute;left:11px;top:544px;background:var(--green);color:#fff;font-size:14px;font-weight:700;padding:5px 10px;border-radius:2px}

/* cover */
.cover{position:absolute;left:230px;top:48px;width:943px;height:362px;background:#fff;overflow:hidden}
.cover svg{position:absolute;left:0;top:0}
.cover__wordmark{position:absolute;left:21px;top:24px;font-family:"Open Sans",sans-serif;font-size:28px;font-weight:300;color:var(--brand-dark)}
.cover__tagline{position:absolute;left:21px;top:58px;font-family:"Open Sans",sans-serif;font-size:25px;font-weight:300;line-height:34px;color:var(--brand)}
.cover__brand{position:absolute;left:24px;top:166px;display:flex;flex-direction:column;align-items:flex-start;gap:10px}
.cover__brand-dot{width:50px;height:50px;border-radius:50%;background:var(--brand-dark)}
.cover__brand-name{font-family:"Open Sans",sans-serif;font-size:20px;font-weight:400;color:var(--brand-dark)}
.services{position:absolute;left:672px;top:22px;width:260px}
.services__title{font-family:"Roboto Condensed",sans-serif;font-weight:700;font-size:32px;color:var(--brand-deep)}
.services__item{position:absolute;left:-4px;width:252px;font-family:"Roboto Condensed",sans-serif;font-size:16px;line-height:19px;color:var(--brand)}
.services__item--second{left:-7px;width:262px}
.contact-band{position:absolute;left:578px;top:268px;color:#fff;font-family:"Roboto Condensed",sans-serif}
.contact-band__address{font-size:21px}
.contact-band__line{font-size:15px;margin-top:6px;white-space:nowrap}
.contact-band__connect{display:flex;align-items:center;gap:9px;font-size:20px;margin-top:14px;padding-left:16px}
.contact-band__circle{width:28px;height:28px;border-radius:50%;border:2px solid #fff}

/* action row */
.actions{position:absolute;left:230px;top:410px;width:943px;height:56px;background:#fff;border-bottom:1px solid var(--line)}
.btn-group{position:absolute;left:15px;top:11px;display:flex;border:1px solid #ccd0d5;border-radius:2px;background:#f6f7f9}
.btn-group span{height:30px;line-height:30px;padding:0 13px;font-size:14px;font-weight:700;color:#4b4f56;border-right:1px solid #ccd0d5}
.btn-group span:last-child{border-right:0}
.btn-primary{position:absolute;left:598px;top:11px;width:160px;height:32px;line-height:32px;text-align:center;background:var(--bar);color:#fff;font-size:15px;border-radius:2px}
.btn-secondary{position:absolute;left:773px;top:11px;width:156px;height:32px;line-height:32px;text-align:center;background:#f6f7f9;border:1px solid #ccd0d5;color:#4b4f56;font-size:15px;border-radius:2px}

/* about card */
.about{position:absolute;left:230px;top:482px;width:943px;height:480px;background:#fff;border:1px solid var(--line);border-radius:3px}
.about__title{position:absolute;left:23px;top:20px;font-size:19px;font-weight:700}
.about__suggest{position:absolute;right:22px;top:22px;font-size:14px;font-weight:700;color:var(--link)}
.info-col{position:absolute;top:76px;width:404px}
.info-col--left{left:32px}
.info-col--right{left:487px;width:422px}
.info-head{font-size:15px;font-weight:700;color:var(--muted);padding-bottom:10px;border-bottom:1px solid #ccd0d5;letter-spacing:.3px}
.info-row{display:flex;gap:10px;margin-top:14px;font-size:15px}
.info-row__icon{width:18px;height:18px;border:1.5px solid #90949c;border-radius:50%;flex:none}
.info-row small{display:block;font-size:13px;line-height:17px;margin-top:6px;width:340px}
.info-link{color:var(--link)}
.team{display:flex;align-items:center;gap:10px;margin-top:20px;font-size:16px;font-weight:700;color:var(--link)}
.team__avatar{width:36px;height:36px;border-radius:50%;background:#b58f70}
</style>
</head>
<body>

<header class="topbar">
  <div class="topbar__mark"></div>
  <div class="topbar__search">VL Consulting<span class="topbar__search-btn"></span></div>
  <nav class="topbar__nav">
    <span class="topbar__user"><span class="topbar__avatar" role="img" aria-label="Member profile photo"></span>Ravindra</span>
    <span class="topbar__link">Home</span>
    <span class="topbar__link">Create</span>
    <span class="topbar__icons">
      <span class="topbar__icon"><span class="topbar__badge">3</span></span>
      <span class="topbar__icon"></span>
      <span class="topbar__icon"><span class="topbar__badge">1</span></span>
      <span class="topbar__icon"></span>
      <span class="topbar__icon"></span>
    </span>
  </nav>
</header>

<aside class="sidebar">
  <div class="profile-pic">
    <span class="profile-pic__dot"></span>
    <span class="profile-pic__name">VL Consulting</span>
  </div>
  <h1 class="page-name">VL Consulting</h1>
  <div class="page-handle">@Valdremoconsulting</div>
  <ul class="page-nav">
    <li>Home</li><li>Photos</li><li>Posts</li>
    <li class="is-active">About</li><li>Community</li><li>Info and ads</li>
  </ul>
  <div class="create-page">Create a Page</div>
</aside>

<section class="cover">
  <svg width="943" height="362" viewBox="0 0 943 362">
    <defs>
      <linearGradient id="photoTone" x1="0" y1="0" x2="1" y2="1">
        <stop offset="0" stop-color="#a9c6e3"/>
        <stop offset="1" stop-color="#5b8fc4"/>
      </linearGradient>
    </defs>
    <polygon points="264,0 666,0 534,362 138,362" fill="url(#photoTone)" role="img" aria-label="Photo of a consultant working at a laptop"/>
    <polygon points="571,253 943,253 943,362 534,362" fill="#093d7a"/>
    <line x1="640" y1="90" x2="661" y2="90" stroke="#093d7a" stroke-width="2"/>
    <circle cx="630" cy="90" r="10" fill="#fff" stroke="#093d7a" stroke-width="3"/>
    <line x1="616" y1="164" x2="657" y2="164" stroke="#093d7a" stroke-width="2"/>
    <circle cx="608" cy="164" r="10" fill="#093d7a" stroke="#fff" stroke-width="3"/>
  </svg>
  <div class="cover__wordmark">VLCONSULTING</div>
  <div class="cover__tagline">Unique Solutions<br>for Business</div>
  <div class="cover__brand">
    <span class="cover__brand-dot"></span>
    <span class="cover__brand-name">VL Consulting</span>
  </div>
  <div class="services">
    <div class="services__title">OUR SERVICES</div>
    <p class="services__item" style="top:58px">Personal Business Coaching to help you start up, manage change or downshift your business.</p>
    <p class="services__item services__item--second" style="top:134px">SME Business Consulting to small and medium enterprises and entrepreneurial clients to help you improve, start or change your business.</p>
  </div>
  <div class="contact-band">
    <div class="contact-band__address">27, Ashgrove Lane, Northwick, NW41 7QD</div>
    <div class="contact-band__line">Tel : +44-7700-900318 &bull; martin.hollis@valdremo.consulting</div>
    <div class="contact-band__connect">Connect with us :
      <span class="contact-band__circle"></span><span class="contact-band__circle"></span><span class="contact-band__circle"></span>
    </div>
  </div>
</section>

<div class="actions">
  <div class="btn-group"><span>Like</span><span>Follow</span><span>Share</span><span>···</span></div>
  <div class="btn-primary">Send Email</div>
  <div class="btn-secondary">Send Message</div>
</div>

<section class="about">
  <h2 class="about__title">About</h2>
  <div class="about__suggest">✎ Suggest Edits</div>
  <div class="info-col info-col--left">
    <div class="info-head">BUSINESS INFO</div>
    <div class="info-row"><span class="info-row__icon"></span>Created in 2016</div>
    <div class="info-row"><span class="info-row__icon"></span><div>Mission<small>To assist new &amp; existing businesses in creating and improving themselves whilst maximising their peoples potential.</small></div></div>
    <div class="info-head" style="margin-top:20px">CONTACT DETAILS</div>
    <div class="info-row"><span class="info-row__icon"></span>Call +44 20 7946 0381</div>
    <div class="info-row"><span class="info-row__icon"></span><span class="info-link">m.me/Valdremoconsulting</span></div>
    <div class="info-row"><span class="info-row__icon"></span><span class="info-link">martin.hollis@valdremo.consulting</span></div>
    <div class="info-row"><span class="info-row__icon"></span><span class="info-link">http://www.valdremo.consulting</span></div>
    <div class="info-head" style="margin-top:18px">MORE INFO</div>
  </div>
  <div class="info-col info-col--right">
    <div class="info-head">TEAM MEMBERS</div>
    <div class="team"><span class="team__avatar" role="img" aria-label="Team member profile photo"></span>Martin Hollis</div>
  </div>
</section>

</body>
</html>
```